New Years In The Smokies - New Years Eve Email Blast

Email blast encouraging guest to reserve their New Years Stay with us - showing the fireworks at The Harbor Row in Pigeon Forge and Gatlinburg's Sky Lantern. I have attached some pictures . Must have phone number 800-362-8105

Target Market(s)

people on email list and social media platforms

Industry/Entity Type

Hotel

Colors
0356a4
85acd3
cedeed

Requirements
Must have
• 800-362-8105
• "Special Rates Available for 12/31 & 1/1"
• http://bramblecrestlodging.com/
Nice to have
• pictures of the area and the celebrations for New Years
Should not have
• not applicable

```html
<!DOCTYPE html>
<html lang="en">
<head>
<meta charset="utf-8">
<title>New Years In The Smokies</title>
<link href="https://fonts.googleapis.com/css2?family=Great+Vibes&family=Oswald:wght@600;700&family=Roboto:wght@400;700;900&display=swap" rel="stylesheet">
<style>
  :root {
    --stage: #e9eaec;
    --night-deep: #2a0508;
    --night-red: #7a0d18;
    --night-glow: #b3182a;
    --gold: #f5c542;
    --gold-light: #ffe9a1;
    --gold-dark: #b8862a;
    --yellow: #ffe100;
    --cta-red: #c3131d;
    --white: #ffffff;
    --brand-blue: #0356a4;
    --sky-blue: #85acd3;
    --mist-blue: #cedeed;
    --photo-night: #14204a;
    --photo-dusk: #6a4a3a;
  }
  * { box-sizing: border-box; margin: 0; padding: 0; }
  html, body { width: 761px; height: 1200px; overflow: hidden; }
  body {
    background: var(--stage);
    font-family: "Roboto", Arial, sans-serif;
    position: relative;
  }
  .email {
    position: absolute;
    left: 145px; top: 30px;
    width: 471px; height: 1140px;
    overflow: hidden;
    background:
      radial-gradient(circle at 50% 28%, var(--night-glow), transparent 55%),
      linear-gradient(180deg, var(--night-deep) 0%, var(--night-red) 32%, var(--night-red) 68%, var(--night-deep) 84%);
  }
  .brand {
    position: absolute; top: 22px; left: 0; width: 100%;
    display: flex; justify-content: center; align-items: center; gap: 8px;
    color: var(--white); font-weight: 900; font-size: 19px; letter-spacing: 1px;
    text-transform: uppercase;
  }
  .brand-dot { width: 14px; height: 14px; border-radius: 50%; background: var(--sky-blue); }
  .headline { position: absolute; top: 74px; width: 100%; text-align: center; }
  .headline-script {
    font-family: "Great Vibes", cursive; font-size: 50px; color: var(--gold-light);
    line-height: 1;
  }
  .headline-year {
    font-family: "Oswald", sans-serif; font-weight: 700; font-size: 124px; line-height: 1;
    color: var(--gold); letter-spacing: 4px; margin-top: -4px;
    text-shadow: 0 3px 0 var(--gold-dark);
  }
  .rates-seal {
    position: absolute; top: 262px; right: 22px;
    width: 76px; height: 76px; border-radius: 50%;
    background: var(--yellow); color: var(--cta-red);
    display: flex; flex-direction: column; justify-content: center; align-items: center;
    font-weight: 900; font-size: 14px; line-height: 1.05; text-transform: uppercase;
    border: 3px solid var(--gold-dark);
    z-index: 2;
  }
  .scene-photo {
    position: absolute; top: 300px; left: 22px; width: 350px; height: 180px;
    transform: rotate(-3deg);
    border: 4px solid var(--white);
    background: linear-gradient(180deg, var(--photo-night) 0%, var(--photo-night) 50%, var(--photo-dusk) 100%);
    box-shadow: 0 6px 14px rgba(0,0,0,.5);
  }
  .copy {
    position: absolute; top: 525px; left: 38px; width: 395px;
    color: var(--white); font-size: 14.5px; line-height: 1.42; text-align: justify;
  }
  .copy p + p { margin-top: 18px; }
  .rates-line {
    position: absolute; top: 695px; width: 100%; text-align: center;
    color: var(--yellow); font-weight: 700; font-size: 19px;
  }
  .book-now {
    position: absolute; top: 732px; left: 132px; width: 208px; height: 42px;
    background: var(--yellow); border-radius: 6px;
    color: var(--cta-red); font-weight: 900; font-size: 24px;
    display: flex; justify-content: center; align-items: center;
    box-shadow: 0 3px 0 var(--gold-dark);
  }
  .phone {
    position: absolute; top: 782px; width: 100%; text-align: center;
    color: var(--white); font-weight: 900; font-size: 38px; letter-spacing: 1px;
    line-height: 1.15;
  }
  .site {
    position: absolute; top: 834px; width: 100%; text-align: center;
    color: var(--white); font-size: 12.5px;
  }
  .wave { position: absolute; top: 860px; left: 0; width: 471px; height: 100px; }
  .partners {
    position: absolute; top: 955px; left: 0; width: 100%; height: 185px;
    background: var(--white);
  }
  .partner-row {
    position: absolute; top: 22px; left: 12px; right: 12px; height: 56px;
    display: grid; grid-template-columns: repeat(4, 1fr); align-items: center;
  }
  .partner {
    display: flex; justify-content: center; align-items: center; gap: 5px;
    font-weight: 700; font-size: 12px; color: var(--brand-blue); white-space: nowrap;
  }
  .partner-mark { width: 12px; height: 12px; background: var(--sky-blue); }
  .partner-badge {
    justify-self: center;
    width: 52px; height: 52px; border-radius: 50%; background: var(--gold);
  }
  .anniversary-badge {
    position: absolute; top: 86px; right: 40px;
    width: 84px; height: 84px; border-radius: 50%;
    background: var(--brand-blue); border: 5px solid var(--gold);
  }
</style>
</head>
<body>
  <main class="email">
    <div class="brand"><span class="brand-dot"></span>Bramblecrest Lodging</div>

    <header class="headline">
      <div class="headline-script">New Year</div>
      <div class="headline-year">2019</div>
    </header>

    <div class="rates-seal"><span>Special</span><span>Rates</span></div>

    <div class="scene-photo" role="img" aria-label="Night photo of New Year fireworks over downtown Gatlinburg and the Sky Lantern"></div>

    <section class="copy">
      <p>New Year’s Eve in the heart of downtown Gatlinburg at the Sky Lantern seems to get bigger and better each year and the 2019 New Year’s Eve ball drop and fireworks is set to be the best one yet!</p>
      <p>Reserve your New Years Stay with us and enjoy the fireworks at The Harbor Row in Pigeon Forge and Gatlinburg’s Sky Lantern!</p>
    </section>

    <div class="rates-line">Special Rates Available for 12/31 &amp; 1/1</div>
    <div class="book-now">BOOK NOW!</div>
    <div class="phone">800-362-8105</div>
    <div class="site">http://bramblecrestlodging.com/</div>

    <svg class="wave" viewBox="0 0 471 100" preserveAspectRatio="none" aria-hidden="true">
      <defs>
        <linearGradient id="waveBlue" x1="0" y1="0" x2="0" y2="1">
          <stop offset="0" stop-color="#0356a4"/>
          <stop offset="1" stop-color="#85acd3"/>
        </linearGradient>
      </defs>
      <path d="M0 35 C120 8 300 65 471 28 L471 100 L0 100 Z" fill="url(#waveBlue)"/>
      <path d="M0 62 C140 40 320 92 471 58 L471 100 L0 100 Z" fill="#cedeed"/>
      <path d="M0 86 C150 70 330 102 471 82 L471 100 L0 100 Z" fill="#ffffff"/>
    </svg>

    <section class="partners">
      <div class="partner-row">
        <div class="partner"><span class="partner-mark"></span>Timber Falls</div>
        <div class="partner-badge" role="img" aria-label="Partner badge"></div>
        <div class="partner">Ridgeline Inn</div>
        <div class="partner">Willowbank Inn</div>
      </div>
      <div class="anniversary-badge" role="img" aria-label="Anniversary badge"></div>
    </section>
  </main>
</body>
</html>
```